Crestmoor Valor Cleaning Solutions

Need a logo and business card design. I want to use a translucent business card. I want to abbreviate the name C.V.C.S. Commercial Cleaning, because my is Tam. I’d also like to incorporate a knight or something like that. I want the idea to tie in with the word Crestmoor. New ideas are welcome, i don’t want to limit anyone’s creativity.

Target Market(s)

Commercial Cleaning for businesses.

Contact Information for Business Card

Crestmoor
Valor
Cleaning
Solutions

```html
<!DOCTYPE html>
<html lang="en">
<head>
<meta charset="utf-8">
<title>Crestmoor Valor Cleaning Solutions — Business Card</title>
<link rel="stylesheet" href="https://fonts.googleapis.com/css2?family=Marcellus&family=Didact+Gothic&display=swap">
<style>
  :root {
    --page-bg: #2a2b2d;
    --navy-deep: #08171e;
    --navy: #112a35;
    --paper: #f7f7f6;
    --paper-shade: #e9e9e8;
    --accent: #29abd4;
    --ink: #1b1b1b;
    --silver: #d9dde0;
  }
  * { box-sizing: border-box; margin: 0; padding: 0; }
  html, body {
    width: 1200px; height: 900px; overflow: hidden;
    background: var(--page-bg);
  }
  .canvas {
    position: relative; width: 1200px; height: 900px;
    font-family: "Didact Gothic", sans-serif;
  }
  .card {
    position: absolute; width: 520px; height: 298px;
    border-radius: 26px;
    box-shadow: 0 18px 40px rgba(0,0,0,.45);
    overflow: hidden;
  }
  .card--front {
    left: 50px; top: 90px;
    background: linear-gradient(135deg, var(--navy) 0%, var(--navy-deep) 100%);
    display: flex; align-items: center; justify-content: center;
  }
  .card--back {
    left: 630px; top: 90px;
    background: linear-gradient(135deg, var(--paper) 40%, var(--paper-shade) 100%);
    display: flex; align-items: center;
    padding: 0 40px 0 44px;
  }
  .brand {
    display: flex; flex-direction: column; align-items: center; text-align: center;
    font-family: "Marcellus", serif;
  }
  .brand__dot {
    width: 54px; height: 54px; border-radius: 50%;
    background: var(--accent);
    margin-bottom: 14px;
  }
  .brand__name {
    font-size: 30px; letter-spacing: 1px; line-height: 1.1;
  }
  .brand__line {
    font-size: 11px; letter-spacing: 5px; margin-top: 6px;
  }
  .card--front .brand { color: var(--silver); }
  .card--back .brand { color: var(--ink); width: 210px; }
  .card--back .brand__dot { width: 44px; height: 44px; }
  .card--back .brand__name { font-size: 21px; }
  .card--back .brand__line { font-size: 8px; letter-spacing: 3.4px; }
  .divider {
    width: 2px; height: 150px; background: var(--accent);
    margin: 0 26px 0 24px;
  }
  .contact__name { font-size: 26px; color: var(--ink); }
  .contact__title { font-size: 15px; color: var(--accent); margin: 2px 0 16px; }
  .contact__list { list-style: none; }
  .contact__item {
    display: flex; align-items: center; gap: 9px;
    font-size: 14px; color: var(--ink); margin-bottom: 7px;
  }
  .contact__icon { width: 14px; height: 14px; flex: none; }
  .lockup {
    position: absolute; left: 0; right: 0; top: 520px;
    display: flex; justify-content: center;
  }
  .lockup .brand { color: var(--silver); }
  .lockup .brand__dot { width: 120px; height: 120px; margin-bottom: 24px; }
  .lockup .brand__name { font-size: 40px; }
  .lockup .brand__line { font-size: 14px; letter-spacing: 7px; margin-top: 8px; }
</style>
</head>
<body>
<main class="canvas">
  <section class="card card--front" aria-label="Card front">
    <div class="brand">
      <span class="brand__dot"></span>
      <span class="brand__name">CRESTMOOR VALOR</span>
      <span class="brand__line">CLEANING SOLUTIONS</span>
    </div>
  </section>

  <section class="card card--back" aria-label="Card back">
    <div class="brand">
      <span class="brand__dot"></span>
      <span class="brand__name">CRESTMOOR VALOR</span>
      <span class="brand__line">CLEANING SOLUTIONS</span>
    </div>
    <div class="divider"></div>
    <div class="contact">
      <p class="contact__name">Your Name</p>
      <p class="contact__title">Job Title</p>
      <ul class="contact__list">
        <li class="contact__item">
          <svg class="contact__icon" viewBox="0 0 16 16"><path fill="#29abd4" d="M3 2h3l1.5 3.5-2 1.2a8 8 0 0 0 3.8 3.8l1.2-2L14 10v3a1 1 0 0 1-1 1A11 11 0 0 1 2 3a1 1 0 0 1 1-1z"/></svg>
          000 000 0000
        </li>
        <li class="contact__item">
          <svg class="contact__icon" viewBox="0 0 16 16"><rect x="1" y="3" width="14" height="10" rx="1" fill="#29abd4"/><path d="M1.5 3.5 8 9l6.5-5.5" stroke="#fff" stroke-width="1.3" fill="none"/></svg>
          youremail@xyz.com
        </li>
        <li class="contact__item">
          <svg class="contact__icon" viewBox="0 0 16 16" fill="none" stroke="#29abd4" stroke-width="1.2"><circle cx="8" cy="8" r="6.5"/><ellipse cx="8" cy="8" rx="3" ry="6.5"/><path d="M1.5 8h13M2.5 5h11M2.5 11h11"/></svg>
          www.yourwebsite.com
        </li>
      </ul>
    </div>
  </section>

  <section class="lockup" aria-label="Logo lockup">
    <div class="brand">
      <span class="brand__dot"></span>
      <span class="brand__name">CRESTMOOR VALOR</span>
      <span class="brand__line">CLEANING SOLUTIONS</span>
    </div>
  </section>
</main>
</body>
</html>
```